agricultural technology company needs business cards*

design a business card that represents our business well. please see our website: halverstonfieldguard.com.au
professional, simple, clean lines, not complicated or floral.....

```html
<!DOCTYPE html>
<html lang="en">
<head>
<meta charset="utf-8">
<title>Halverston FieldGuard – Business Cards</title>
<link href="https://fonts.googleapis.com/css2?family=Archivo:wght@500;700;800&family=Roboto:wght@400;500&display=swap" rel="stylesheet">
<style>
  :root {
    --navy: #1d2d5e;
    --green: #2bb04a;
    --lime: #a3cb3b;
    --white: #ffffff;
    --bg: #e4e6ea;
    --ink: #1d2d5e;
  }
  * { box-sizing: border-box; margin: 0; padding: 0; }
  html, body { width: 1200px; height: 901px; overflow: hidden; }
  body {
    background: var(--bg);
    font-family: "Roboto", Arial, sans-serif;
    display: flex;
    align-items: center;
    justify-content: center;
    gap: 50px;
  }
  .card {
    width: 540px;
    height: 309px;
    position: relative;
    overflow: hidden;
    box-shadow: 0 10px 28px rgba(0,0,0,0.22);
  }
  /* Back of card */
  .card-back {
    background: var(--navy);
    color: var(--white);
  }
  .card-back .faint-decoration {
    position: absolute;
    left: 60px; top: 0;
    width: 220px; height: 309px;
    background: radial-gradient(ellipse at 40% 45%, rgba(255,255,255,0.07), rgba(255,255,255,0) 70%);
  }
  .card-back .brand {
    position: absolute;
    left: 0; right: 0; top: 112px;
    text-align: center;
    font-family: "Archivo", Arial, sans-serif;
    font-weight: 800;
    font-size: 40px;
    letter-spacing: -0.5px;
    color: var(--white);
    line-height: 1.05;
  }
  .card-back .brand-url {
    position: absolute;
    left: 0; right: 0; top: 178px;
    text-align: center;
    font-size: 14px;
    letter-spacing: 0.6px;
  }
  .card-back .site {
    position: absolute;
    left: 0; right: 0; bottom: 34px;
    text-align: center;
    font-size: 16px;
    letter-spacing: 0.8px;
  }
  /* Front of card */
  .card-front { background: var(--white); }
  .card-front .leaf-art {
    position: absolute;
    left: 0; top: 0;
    width: 300px; height: 309px;
  }
  .card-front .details {
    position: absolute;
    right: 26px; top: 34px;
    text-align: right;
    color: var(--ink);
  }
  .details .brand {
    font-family: "Archivo", Arial, sans-serif;
    font-weight: 800;
    font-size: 22px;
    color: var(--navy);
    letter-spacing: -0.3px;
    margin-bottom: 18px;
  }
  .details .person-name {
    font-size: 20px;
    font-weight: 500;
    color: var(--green);
  }
  .details .person-role {
    font-size: 13px;
    margin-bottom: 16px;
  }
  .details .address {
    font-size: 12.5px;
    line-height: 1.35;
    margin-bottom: 12px;
  }
  .details .contact-line {
    font-size: 12.5px;
    line-height: 1.55;
    display: flex;
    justify-content: flex-end;
    align-items: center;
    gap: 8px;
  }
  .contact-line .url-accent { color: var(--green); }
  .contact-line svg { width: 11px; height: 11px; flex: none; }
</style>
</head>
<body>

  <section class="card card-back">
    <div class="faint-decoration" role="img" aria-label="Faint brand leaf decoration"></div>
    <div class="brand">Halverston FieldGuard</div>
    <div class="brand-url">halverstonfieldguard.com.au</div>
    <div class="site">www.halverstonfieldguard.com.au</div>
  </section>

  <section class="card card-front">
    <svg class="leaf-art" viewBox="0 0 300 309" role="img" aria-label="Large green leaf decoration">
      <defs>
        <linearGradient id="leafTone" x1="0" y1="0" x2="1" y2="0">
          <stop offset="0" stop-color="#a3cb3b"/>
          <stop offset="1" stop-color="#2bb04a"/>
        </linearGradient>
      </defs>
      <path d="M0 0 H230 C160 60 130 140 170 200 C195 240 240 280 300 309 H0 Z" fill="url(#leafTone)"/>
    </svg>

    <div class="details">
      <div class="brand">Halverston FieldGuard</div>
      <div class="person-name">Marcus Dellow</div>
      <div class="person-role">Manager</div>
      <div class="address">52 Tarlow Street,<br>Kwinana, WA 6170</div>
      <div class="contact-line">1300 482 316
        <svg viewBox="0 0 12 12"><path d="M2 1 L4.5 1 L5.5 3.5 L4 4.5 C4.7 6 6 7.3 7.5 8 L8.5 6.5 L11 7.5 L11 10 C6 10.5 1.5 6 2 1 Z" fill="var(--green)"/></svg>
      </div>
      <div class="contact-line">office@halverstonfieldguard.com.au
        <svg viewBox="0 0 12 12"><rect x="1" y="2.5" width="10" height="7" fill="none" stroke="var(--green)" stroke-width="1.2"/><path d="M1 2.5 L6 6.5 L11 2.5" fill="none" stroke="var(--green)" stroke-width="1.2"/></svg>
      </div>
      <div class="contact-line">www.<span class="url-accent">halverstonfieldguard</span>.com.au
        <svg viewBox="0 0 12 12"><circle cx="6" cy="6" r="5" fill="none" stroke="var(--green)" stroke-width="1.2"/><path d="M1 6 H11 M6 1 C3.5 4 3.5 8 6 11 M6 1 C8.5 4 8.5 8 6 11" fill="none" stroke="var(--green)" stroke-width="1"/></svg>
      </div>
    </div>
  </section>

</body>
</html>
```